Create and Design Brand Guidelines for IT Company

Verlo Networks Logo and Branding Objective
Verlo Networks is upgrading its brand assets, marketing collateral and website. The company is seeking a graphic designer's expertise to develop a style guide that creates brand consistency and communicates to internal and external stakeholders how to position the Verlo Networks brand when assigned tasks relating to the brand. The brand style guide should have information about the logo and clear usage guidelines, a recommended font to use, a colour profile including HEX code, RGB, CMYK, Pantone codes, and iconography recommendations. Details about the company tone, voice and photography usage will be added by Verlo Networks.
Look and feel
Each slider illustrates characteristics of the customer's brand and the style your logo design should communicate.

```html
<!DOCTYPE html>
<html lang="en">
<head>
<meta charset="utf-8">
<title>Verlo Networks — Design &amp; Brand Manual</title>
<link href="https://fonts.googleapis.com/css2?family=Jost:wght@400;500;700&display=swap" rel="stylesheet">
<style>
  :root {
    --backdrop: #2b2a28;
    --page: #e9eaea;
    --page-light: #f7f7f7;
    --ink: #1f1f1f;
    --ink-soft: #3a3a3a;
    --brand-blue: #007ec3;
    --brand-grey: #9aa8b3;
    --brand-gold: #dea514;
    --panel-dark: #2b2a28;
    --rule: #9a9a9a;
  }
  * { box-sizing: border-box; margin: 0; padding: 0; }
  html, body { width: 1171px; height: 1200px; overflow: hidden; }
  body {
    background: var(--backdrop);
    font-family: "Jost", "Futura", sans-serif;
    color: var(--ink);
    position: relative;
  }
  .page {
    position: absolute;
    width: 481px; height: 328px;
    background: radial-gradient(ellipse at 50% 40%, var(--page-light) 0%, var(--page) 70%, #dedfdf 100%);
  }
  .page--1 { left: 90px;  top: 79px; }
  .page--2 { left: 600px; top: 79px; }
  .page--3 { left: 90px;  top: 436px; }
  .page--4 { left: 600px; top: 436px; }
  .page--5 { left: 90px;  top: 792px; }
  .page--6 { left: 600px; top: 792px; }

  .abs { position: absolute; }
  .wordmark { position: absolute; font-weight: 500; white-space: nowrap; letter-spacing: 0.5px; line-height: 1; }

  .section-title {
    position: absolute; left: 34px;
    font-size: 11px; font-weight: 400; line-height: 1.3; text-transform: uppercase; color: var(--ink-soft);
  }
  .body-col {
    position: absolute; width: 142px;
    font-size: 4.6px; line-height: 1.5; color: var(--ink-soft);
  }
  .body-col p + p { margin-top: 5px; }

  .page-footer {
    position: absolute; left: 16px; right: 16px; bottom: 7px;
    display: flex; align-items: center; gap: 6px;
    font-size: 4.4px; text-transform: uppercase; color: var(--ink-soft);
  }
  .page-footer .rule { flex: 1; height: 0; border-top: 0.5px solid var(--rule); }

  .swatch { position: absolute; width: 26px; height: 26px; }
  .swatch--blue { background: var(--brand-blue); }
  .swatch--grey { background: var(--brand-grey); }
  .swatch-spec { position: absolute; font-family: Arial, sans-serif; font-size: 5.6px; line-height: 1.55; color: var(--ink-soft); }

  .dark-panel { position: absolute; left: 228px; top: 51px; width: 177px; height: 91px; background: var(--panel-dark); }

  .variant {
    position: absolute; width: 91px; height: 47px;
    display: flex; align-items: center; justify-content: center;
    font-size: 10px; font-weight: 500;
  }
  .variant--plain { background: transparent; color: var(--brand-blue); }
  .variant--blue { background: var(--brand-blue); color: #ffffff; }
  .variant--gold { background: var(--brand-gold); color: var(--ink); }
  .variant--sky { background: linear-gradient(135deg, #dfe7f0, #b9c9dc 60%, #e7edf3); color: var(--brand-blue); }
  .variant--desk { background: linear-gradient(135deg, #5a4d43, #a89584 55%, #3c3733); color: var(--brand-blue); }
  .variant--bright { background: linear-gradient(90deg, #f4f2ef, #dcd8d2 60%, #bcb6ae); color: var(--ink); }

  .size-label { position: absolute; font-size: 4.8px; line-height: 1.4; color: var(--ink-soft); }

  .type-name { position: absolute; left: 30px; font-size: 11px; color: var(--ink-soft); }
  .type-sample { position: absolute; right: 28px; text-align: right; font-size: 11px; line-height: 1.25; color: var(--ink); letter-spacing: 0.2px; }
  .bold { font-weight: 700; }
</style>
</head>
<body>

<!-- Page 1: Philosophy -->
<section class="page page--1">
  <div class="wordmark" style="left:70px;top:56px;font-size:30px;color:var(--ink);">Verlo Networks</div>
  <h2 class="section-title" style="top:201px;">Philosophy<br>Logo</h2>
  <div class="body-col" style="left:146px;top:203px;">
    <p>The Verlo Networks brand identity is built on a unique logo that summarizes all the principles of its mission.</p>
    <p>The identity favours clean geometry, open spacing and calm tones. Every element follows the same logic, so each touchpoint reads as one voice. The mark is set in a modern sans serif with even strokes, chosen to reflect precision and reliability. Proportions stay fixed across print, screen and signage. Colour and type support each other, giving the brand a clear, confident and technical character that partners and clients can recognise at a glance.</p>
  </div>
  <div class="body-col" style="left:296px;top:203px;">
    <p>The system is designed to scale from small icons to large displays without losing clarity. Layouts rely on a simple grid, generous margins and a restrained palette. Staff and partners should follow these rules whenever they prepare materials, so the brand stays consistent in every channel, from documents and slides to the website, packaging and events.</p>
  </div>
  <footer class="page-footer"><span>Design &amp; Brand Manual</span><span class="rule"></span><span>1</span></footer>
</section>

<!-- Page 2: Basic version -->
<section class="page page--2">
  <div class="wordmark" style="left:132px;top:58px;font-size:30px;color:var(--brand-blue);">Verlo Networks</div>
  <div class="swatch swatch--blue" style="left:134px;top:135px;"></div>
  <div class="swatch-spec" style="left:180px;top:135px;">CMYK 85/40/0/0<br>RGB 0/126/195<br>HEX #007EC3</div>
  <div class="swatch swatch--grey" style="left:258px;top:135px;"></div>
  <div class="swatch-spec" style="left:304px;top:135px;">CMYK 85/40/0/0<br>RGB 0/126/195<br>HEX #007EC3</div>
  <h2 class="section-title" style="top:203px;">Basic version<br>full color<br>logo</h2>
  <div class="body-col" style="left:160px;top:203px;">
    <p>The basic version of the logo is the main representative of the identity and consists of two basic units - typographic and sub text part. The dominant typography consists of the brand name "Verlo" in a characteristic blue color. The sub text part of the logo is represented by a grey square, which complements and represents the logo both the technical sophistication of the brand and its ecological direction.</p>
  </div>
  <div class="body-col" style="left:311px;top:203px;">
    <p>It is essential to maintain the logo in all cases shape and color fidelity, showing the shape principles the visualized design of the logo and the color are defined by the table with color profile conversions. For optimal logo look was during its construction, a defined ratio of individual colors, which it is characterized by - it is important to keep in all used color profiles. If the method of reproduction allows, it is always necessary to use full color version of the logo. The logo cannot be recolored color spectrum than the defined</p>
  </div>
  <footer class="page-footer"><span>Design &amp; Brand Manual</span><span class="rule"></span><span>2</span></footer>
</section>

<!-- Page 3: Monochromatic -->
<section class="page page--3">
  <div class="wordmark" style="left:88px;top:86px;font-size:17px;color:var(--ink);">Verlo Networks</div>
  <div class="dark-panel">
    <div class="wordmark" style="left:23px;top:37px;font-size:17px;color:#ffffff;">Verlo Networks</div>
  </div>
  <h2 class="section-title" style="top:209px;">Monochromatic<br>logo version</h2>
  <div class="body-col" style="left:146px;top:211px;">
    <p>Due to the wide need to use the logo across different media and technological possibilities for reproduction is needed determine the logo of its color variants. By defining precise rules in the color degradation of the logo from full-color to monochrome versions, it is ensured that the logo is used correctly with regard to reproduction limits</p>
  </div>
  <div class="body-col" style="left:296px;top:211px;">
    <p>Monochrome variants of the logo for light and dark backgrounds are used primarily in cases of impossibility of quality reproduction, in which the color, the logos, would lose if the character required it in the case of placement of the logo on partners materials outside the Verlo Networks color spectrum</p>
  </div>
  <footer class="page-footer"><span>Design &amp; Brand Manual</span><span class="rule"></span><span>3</span></footer>
</section>

<!-- Page 4: Permitted variants -->
<section class="page page--4">
  <div class="variant variant--plain" style="left:81px;top:38px;">Verlo Networks</div>
  <div class="variant variant--blue" style="left:187px;top:38px;">Verlo Networks</div>
  <div class="variant variant--gold" style="left:293px;top:38px;">Verlo Networks</div>
  <div class="variant variant--sky" style="left:81px;top:100px;" role="img" aria-label="Logo placed on a pale sky photograph">Verlo Networks</div>
  <div class="variant variant--desk" style="left:187px;top:100px;" role="img" aria-label="Logo placed on a photograph of a desk with a laptop">Verlo Networks</div>
  <div class="variant variant--bright" style="left:293px;top:100px;" role="img" aria-label="Logo placed on a bright interior photograph">Verlo Networks</div>
  <h2 class="section-title" style="top:210px;">Logo and its<br>color permitted<br>variants</h2>
  <div class="body-col" style="left:160px;top:213px;">
    <p>The table indicates the use of logo variants due to the nature and color of the substrate. Due to the color nature of the logo, it is necessary to manage when placing it on the basis set by the rules defined in the scheme. No other combination variations are allowed.<br>The logo can be placed on colored surfaces corresponding to corporate colors, on substrates outside the color range of corporate colors Verlo as well as photos. However, it is necessary to follow the rule of sufficient visibility and contrast.</p>
  </div>
  <div class="body-col" style="left:311px;top:213px;">
    <p>When applying the logo on a white background, we use the logo in the base colors. In case of application on a substrate in corporate color we use a white monochrome variant of the logo. In case of application we use black monochrome on the background outside the color palette logo variants. It is permitted to apply both monochrome and full-color logos to the photographic substrate, as long as the color of the substrate allows. The monochrome version of the logo is only allowed if it is not possible use a color version or the nature of the reproduction does not allow it material technology</p>
  </div>
  <footer class="page-footer"><span>Design &amp; Brand Manual</span><span class="rule"></span><span>4</span></footer>
</section>

<!-- Page 5: Minimum sizes -->
<section class="page page--5">
  <svg class="abs" style="left:0;top:0;" width="481" height="140" aria-hidden="true">
    <line x1="92" y1="41" x2="400" y2="41" stroke="#555" stroke-width="0.6" stroke-dasharray="1.2 1.2"/>
    <line x1="92" y1="129" x2="400" y2="129" stroke="#555" stroke-width="0.6" stroke-dasharray="1.2 1.2"/>
    <line x1="92" y1="42" x2="92" y2="128" stroke="#555" stroke-width="0.6" stroke-dasharray="1.2 1.2"/>
    <path d="M90.5 44 L92 41 L93.5 44 M90.5 126 L92 129 L93.5 126" fill="none" stroke="#555" stroke-width="0.6"/>
  </svg>
  <div class="abs" style="left:36px;top:89px;font-size:11px;color:var(--ink-soft);">5mm</div>
  <div class="wordmark" style="left:108px;top:68px;font-size:40px;color:var(--brand-blue);">Verlo Networks</div>
  <div class="wordmark" style="left:168px;top:151px;font-size:8px;color:var(--brand-blue);">Verlo Networks</div>
  <div class="size-label" style="left:168px;top:166px;">real size (5mm)<br>color version</div>
  <div class="wordmark" style="left:250px;top:151px;font-size:8px;color:var(--ink);">Verlo Networks</div>
  <div class="size-label" style="left:250px;top:166px;">real size (3mm)<br>b / w version</div>
  <h2 class="section-title" style="top:215px;">Minimum sizes<br>logo appearance<br>for format</h2>
  <div class="body-col" style="left:146px;top:217px;">
    <p>Optimal identity on any standardized formats is also given by compliance with the recommended resp. minimum logo size. The ratio of individual components or their the mutual size does not change in any way. The minimum size of the logo used on any formats size is 5 mm for the basic color version of the logo and 3 mm for monochrome variant</p>
  </div>
  <footer class="page-footer" style="left:21px;right:11px;"><span>Design &amp; Brand Manual</span><span class="rule"></span><span>5</span></footer>
</section>

<!-- Page 6: Basic font -->
<section class="page page--6">
  <div class="type-name" style="top:55px;">FUTURA Md BT</div>
  <div class="type-sample" style="top:57px;">ABCDEFGHIJKLMNOPQRSTUVWXYZ<br>ABCDEFGHIJKLMNOPQRSTUVWXYZ<br>1234567890</div>
  <div class="type-name bold" style="top:111px;">FUTURA Md BT BOLD</div>
  <div class="type-sample bold" style="top:110px;">ABCDEFGHIJKLMNOPQRSTUVWXYZ<br>ABCDEFGHIJKLMNOPQRSTUVWXYZ<br>1234567890</div>
  <h2 class="section-title" style="top:215px;left:30px;">Basic font</h2>
  <div class="body-col" style="left:160px;top:217px;">
    <p>The basic corporate font of Korrin is the Futura T CE family. Its visual simplicity and variability of use support the overall impression and emphasize the characteristic profile of the brand. Quantity The cuts that this font has are creating creates a wide manipulation space for typographic game</p>
  </div>
  <div class="body-col" style="left:311px;top:217px;">
    <p>The sans serif, referring to the functionalist tradition, works factually but significantly. It is used in printed matter for all text materials except in cases where it is necessary to use the system font. By this cases are mainly areas of electronic and online communication. It is recommended to use the Arial system font in this area</p>
  </div>
  <footer class="page-footer" style="left:21px;right:11px;"><span>Design &amp; Brand Manual</span><span class="rule"></span><span>6</span></footer>
</section>

</body>
</html>
```